Endocrinologist needs new stationery

I have a logo from MarkForge and now need stationery with the new logo.

Address: Suite 4, 282 Falcon Street, Richmond, VIC 3121
Phone: 03 9417 2253
Fax: 03 9417 2255
Website: www.drmaylacorwen.com.au
Email: admin@drmaylacorwen.com.au

```html
<!DOCTYPE html>
<html lang="en">
<head>
<meta charset="utf-8">
<title>Dr Mayla Corwen Endocrinology – Stationery</title>
<link href="https://fonts.googleapis.com/css2?family=Arimo:wght@400;700&family=Cormorant+Garamond:wght@400;500&family=Montserrat:wght@500&display=swap" rel="stylesheet">
<style>
:root{
  --brand-blue:#4a78a3;
  --brand-mauve:#8a6a7f;
  --stage-blue:#4473a0;
  --stage-plum:#7d6375;
  --board-dark:#2d3a44;
  --paper:#ffffff;
  --ink:#222222;
  --rule:#c9d3dd;
  --label:#b9c2c9;
}
*{margin:0;padding:0;box-sizing:border-box}
html,body{width:1200px;height:2567px;overflow:hidden}
body{position:relative;background:var(--board-dark);font-family:"Arimo",Arial,sans-serif;color:var(--ink)}
.stage{position:absolute;left:0;top:0;width:1200px;height:1180px;background:linear-gradient(var(--stage-blue) 0 560px,var(--stage-plum) 560px)}
.brand{position:absolute;font-family:"Cormorant Garamond",serif;color:var(--brand-blue);white-space:nowrap}
.brand-name{font-weight:400;display:block}
.hero-brand{left:70px;top:62px;color:#fff}
.hero-brand .brand-name{font-size:58px;line-height:1}
.hero-brand .brand-sub{display:flex;align-items:center;gap:14px;font-size:17px;letter-spacing:10px;margin-top:8px}
.hero-brand .brand-sub::after{content:"";width:82px;height:1px;background:#fff}
.hero-letter{position:absolute;left:290px;top:230px;transform:scale(1.35);transform-origin:0 0;box-shadow:0 20px 40px rgba(0,0,0,.25)}
.section-label{position:absolute;font-family:"Montserrat",sans-serif;font-weight:500;font-size:12px;letter-spacing:4px;color:var(--label)}
.page{position:absolute;width:460px;height:650px;background:var(--paper);overflow:hidden}
.page .brand .brand-name{font-size:21px;line-height:1}
.page .brand .brand-sub{font-size:6px;letter-spacing:5.5px;display:block;margin-top:1px}
.head-rule{position:absolute;height:1px;background:var(--brand-blue)}
.contact{position:absolute;font-family:"Cormorant Garamond",serif;font-size:5px;color:var(--brand-blue);display:flex;align-items:center;gap:3px;white-space:nowrap}
.contact svg{width:6px;height:6px}
.letter{position:absolute;left:43px;top:118px;width:374px;font-size:7px;line-height:10.1px}
.letter .date{margin-bottom:21px}
.letter .recipient-name{font-weight:700;font-size:8px}
.letter .recipient{margin-bottom:21px}
.letter p.body{text-align:justify;margin-bottom:10px}
.letter .salutation{margin-bottom:10px}
.sign-off{margin-top:30px}
.signature{width:78px;height:14px;background:linear-gradient(90deg,#555 0,#999 100%);opacity:.35;border-radius:3px;margin:2px 0 1px}
.sign-name{font-weight:700;font-size:8px}
.foot-rule{position:absolute;left:43px;width:374px;top:612px;height:1px;background:var(--rule)}
.page-alt2 .tab{position:absolute;left:0;top:28px;width:4px;height:30px;background:var(--brand-mauve)}
.notepad{position:absolute;left:449px;top:2057px;width:306px;height:433px;background:var(--paper)}
.notepad .tab{position:absolute;left:0;top:18px;width:3px;height:20px;background:var(--brand-mauve)}
.notepad .brand .brand-name{font-size:15px;line-height:1}
.notepad .brand .brand-sub{font-size:4.5px;letter-spacing:4px;display:block}
.date-field{position:absolute;left:211px;top:14px;font-family:"Cormorant Garamond",serif;font-size:5px;color:#555;display:flex;align-items:center;gap:5px}
.date-field span{display:block;width:56px;height:10px;border:1px solid #e3e6ea}
.lines{position:absolute;left:24px;top:52px;width:258px;height:345px;background:repeating-linear-gradient(transparent 0 13.4px,#edf0f3 13.4px 14.4px)}
</style>
</head>
<body>

<section class="stage">
  <div class="brand hero-brand"><span class="brand-name">Dr Mayla Corwen</span><span class="brand-sub">ENDOCRINOLOGY</span></div>

  <article class="page hero-letter">
    <div class="head-rule" style="left:43px;top:53px;width:105px"></div>
    <div class="head-rule" style="left:312px;top:53px;width:105px"></div>
    <div class="brand" style="left:152px;top:26px;text-align:center"><span class="brand-name">Dr Mayla Corwen</span><span class="brand-sub">ENDOCRINOLOGY</span></div>
    <div class="contact" style="left:43px;top:60px"><svg viewBox="0 0 10 10"><rect x="1" y="2" width="8" height="6" fill="none" stroke="currentColor"/><path d="M1 2l4 3 4-3" fill="none" stroke="currentColor"/></svg>admin@drmaylacorwen.com.au</div>
    <div class="contact" style="left:318px;top:60px"><svg viewBox="0 0 10 10"><path d="M2 1l2 0 1 2-1 1q1 2 3 3l1-1 2 1 0 2q-6 0-8-8z" fill="currentColor"/></svg>03 9417 2253</div>
    <div class="contact" style="left:377px;top:60px"><svg viewBox="0 0 10 10"><rect x="1" y="3" width="8" height="5" fill="none" stroke="currentColor"/><rect x="3" y="1" width="4" height="2" fill="currentColor"/></svg>03 9417 2255</div>
    <div class="letter">
      <div class="date">8 May 2026</div>
      <div class="recipient"><div class="recipient-name">DANIEL WESTBROOK</div>Department Head<br>6120 Orchard Road,<br>Richmond, VIC 3121</div>
      <div class="salutation">Dear Mr. Westbrook,</div>
      <p class="body">Lorem ipsum dolor sit amet consectetur. Magna vitae platea cras sed auctor ultrices facilisis auctor. Ultrices sit purus cursus vitae turpis elit tortor ullamcorper. Velit mi et ac dictumst vitae elementum scelerisque sagittis habitant. Id massa tortor adipiscing volutpat vitae tellus. Ipsum ullamcorper enim justo mus elementum enim odio. Mattis quis sagittis aliquet dui vitae in ut morbi sit. Dignissim et posuere sed tristique. At in mattis odio adipiscing imperdiet facilisi morbi ipsum. Gravida tincidunt quis ipsum faucibus risus. Risus et faucibus cursus gravida consequat.</p>
      <p class="body">Tristique blandit cursus nisl non sit diam duis. Eros congue eu varius orci neque nisl laoreet. Volutpat orci faucibus risus elementum arcu pulvinar ut mattis tincidunt. Eu felis adipiscing ut risus egestas convallis. Adipiscing feugiat pharetra imperdiet cursus ultrices. Penatibus quis cursus mollis adipiscing.</p>
      <p class="body">Nunc lectus mi sed enim nisi pretium enim augue. Aliquam quam amet in diam in arcu. Tincidunt vulputate augue quam in eu. Urna tortor iaculis enim turpis fringilla sagittis at et faucibus. Nunc eu purus sit hendrerit. Sit lacus a tristique sed in nibh rutrum faucibus. Accumsan orci iaculis sit morbi sit tortor facilisis. Odio turpis massa sit non facilisi risus. Elementum eu id vitae arcu porta ridiculus. Eget orci enim lacus sed est in egestas maecenas nisi. Eget ultrices lectus tincidunt in laoreet duis nulla. Faucibus consectetur tincidunt aenean sed vitae velit imperdiet. Ut cursus amet pharetra vivamus. Aliquam eleifend aliquam tortor lorem feugiat nisl. Faucibus enim diam at sed senectus nam duis.</p>
      <p class="body">At ultrices risus in ante est praesent. Aliquam gravida condimentum non sed semper. Arcu ornare odio tincidunt in a eu netus nec mattis.</p>
      <div class="sign-off">Thanks,</div>
      <div class="signature" role="img" aria-label="Handwritten signature"></div>
      <div class="sign-name">DR MAYLA CORWEN</div>
      <div>MD FRACP FRCPC PhD BSc</div>
      <div>Consultant Endocrinologist</div>
    </div>
    <div class="foot-rule"></div>
    <div class="contact" style="left:43px;top:621px"><svg viewBox="0 0 10 10"><path d="M5 9Q1 5 1 4a4 4 0 0 1 8 0q0 1-4 5z" fill="none" stroke="currentColor"/><circle cx="5" cy="4" r="1.3" fill="currentColor"/></svg>Suite 4, 282 Falcon Street, Richmond, VIC 3121</div>
    <div class="contact" style="right:43px;top:621px">www.drmaylacorwen.com.au<svg viewBox="0 0 10 10"><circle cx="5" cy="5" r="4" fill="currentColor"/></svg></div>
  </article>
</section>

<h2 class="section-label" style="left:106px;top:1265px">LETTERHEAD DESIGN ALT 1</h2>
<h2 class="section-label" style="left:638px;top:1265px">LETTERHEAD DESIGN ALT 2</h2>

<article class="page page-alt1" style="left:106px;top:1294px">
  <div class="head-rule" style="left:43px;top:53px;width:105px"></div>
  <div class="head-rule" style="left:312px;top:53px;width:105px"></div>
  <div class="brand" style="left:152px;top:26px"><span class="brand-name">Dr Mayla Corwen</span><span class="brand-sub">ENDOCRINOLOGY</span></div>
  <div class="contact" style="left:43px;top:60px"><svg viewBox="0 0 10 10"><rect x="1" y="2" width="8" height="6" fill="none" stroke="currentColor"/><path d="M1 2l4 3 4-3" fill="none" stroke="currentColor"/></svg>admin@drmaylacorwen.com.au</div>
  <div class="contact" style="left:318px;top:60px"><svg viewBox="0 0 10 10"><path d="M2 1l2 0 1 2-1 1q1 2 3 3l1-1 2 1 0 2q-6 0-8-8z" fill="currentColor"/></svg>03 9417 2253</div>
  <div class="contact" style="left:377px;top:60px"><svg viewBox="0 0 10 10"><rect x="1" y="3" width="8" height="5" fill="none" stroke="currentColor"/><rect x="3" y="1" width="4" height="2" fill="currentColor"/></svg>03 9417 2255</div>
  <div class="letter">
    <div class="date">8 May 2026</div>
    <div class="recipient"><div class="recipient-name">DANIEL WESTBROOK</div>Department Head<br>6120 Orchard Road,<br>Richmond, VIC 3121</div>
    <div class="salutation">Dear Mr. Westbrook,</div>
    <p class="body">Lorem ipsum dolor sit amet consectetur. Magna vitae platea cras sed auctor ultrices facilisis auctor. Ultrices sit purus cursus vitae turpis elit tortor ullamcorper. Velit mi et ac dictumst vitae elementum scelerisque sagittis habitant. Id massa tortor adipiscing volutpat vitae tellus. Ipsum ullamcorper enim justo mus elementum enim odio. Mattis quis sagittis aliquet dui vitae in ut morbi sit. Dignissim et posuere sed tristique. At in mattis odio adipiscing imperdiet facilisi morbi ipsum. Gravida tincidunt quis ipsum faucibus risus. Risus et faucibus cursus gravida consequat.</p>
    <p class="body">Tristique blandit cursus nisl non sit diam duis. Eros congue eu varius orci neque nisl laoreet. Volutpat orci faucibus risus elementum arcu pulvinar ut mattis tincidunt. Eu felis adipiscing ut risus egestas convallis. Adipiscing feugiat pharetra imperdiet cursus ultrices. Penatibus quis cursus mollis adipiscing.</p>
    <p class="body">Nunc lectus mi sed enim nisi pretium enim augue. Aliquam quam amet in diam in arcu. Tincidunt vulputate augue quam in eu. Urna tortor iaculis enim turpis fringilla sagittis at et faucibus. Nunc eu purus sit hendrerit. Sit lacus a tristique sed in nibh rutrum faucibus. Accumsan orci iaculis sit morbi sit tortor facilisis. Odio turpis massa sit non facilisi risus. Elementum eu id vitae arcu porta ridiculus. Eget orci enim lacus sed est in egestas maecenas nisi. Eget ultrices lectus tincidunt in laoreet duis nulla. Faucibus consectetur tincidunt aenean sed vitae velit imperdiet. Ut cursus amet pharetra vivamus. Aliquam eleifend aliquam tortor lorem feugiat nisl. Faucibus enim diam at sed senectus nam duis.</p>
    <p class="body">At ultrices risus in ante est praesent. Aliquam gravida condimentum non sed semper. Arcu ornare odio tincidunt in a eu netus nec mattis.</p>
    <div class="sign-off">Thanks,</div>
    <div class="signature" role="img" aria-label="Handwritten signature"></div>
    <div class="sign-name">DR MAYLA CORWEN</div>
    <div>MD FRACP FRCPC PhD BSc</div>
    <div>Consultant Endocrinologist</div>
  </div>
  <div class="foot-rule"></div>
  <div class="contact" style="left:43px;top:621px"><svg viewBox="0 0 10 10"><path d="M5 9Q1 5 1 4a4 4 0 0 1 8 0q0 1-4 5z" fill="none" stroke="currentColor"/><circle cx="5" cy="4" r="1.3" fill="currentColor"/></svg>Suite 4, 282 Falcon Street, Richmond, VIC 3121</div>
  <div class="contact" style="right:43px;top:621px">www.drmaylacorwen.com.au<svg viewBox="0 0 10 10"><circle cx="5" cy="5" r="4" fill="currentColor"/></svg></div>
</article>

<article class="page page-alt2" style="left:638px;top:1294px">
  <div class="tab"></div>
  <div class="brand" style="left:43px;top:30px"><span class="brand-name">Dr Mayla Corwen</span><span class="brand-sub">ENDOCRINOLOGY</span></div>
  <div class="head-rule" style="left:170px;top:56px;width:247px;background:var(--brand-mauve)"></div>
  <div class="contact" style="left:347px;top:21px"><svg viewBox="0 0 10 10"><path d="M2 1l2 0 1 2-1 1q1 2 3 3l1-1 2 1 0 2q-6 0-8-8z" fill="currentColor"/></svg>03 9417 2253</div>
  <div class="contact" style="left:347px;top:32px"><svg viewBox="0 0 10 10"><rect x="1" y="3" width="8" height="5" fill="none" stroke="currentColor"/><rect x="3" y="1" width="4" height="2" fill="currentColor"/></svg>03 9417 2255</div>
  <div class="contact" style="left:347px;top:43px"><svg viewBox="0 0 10 10"><rect x="1" y="2" width="8" height="6" fill="none" stroke="currentColor"/><path d="M1 2l4 3 4-3" fill="none" stroke="currentColor"/></svg>admin@drmaylacorwen.com.au</div>
  <div class="letter">
    <div class="date">8 May 2026</div>
    <div class="recipient"><div class="recipient-name">DANIEL WESTBROOK</div>Department Head<br>6120 Orchard Road,<br>Richmond, VIC 3121</div>
    <div class="salutation">Dear Mr. Westbrook,</div>
    <p class="body">Lorem ipsum dolor sit amet consectetur. Magna vitae platea cras sed auctor ultrices facilisis auctor. Ultrices sit purus cursus vitae turpis elit tortor ullamcorper. Velit mi et ac dictumst vitae elementum scelerisque sagittis habitant. Id massa tortor adipiscing volutpat vitae tellus. Ipsum ullamcorper enim justo mus elementum enim odio. Mattis quis sagittis aliquet dui vitae in ut morbi sit. Dignissim et posuere sed tristique. At in mattis odio adipiscing imperdiet facilisi morbi ipsum. Gravida tincidunt quis ipsum faucibus risus. Risus et faucibus cursus gravida consequat.</p>
    <p class="body">Tristique blandit cursus nisl non sit diam duis. Eros congue eu varius orci neque nisl laoreet. Volutpat orci faucibus risus elementum arcu pulvinar ut mattis tincidunt. Eu felis adipiscing ut risus egestas convallis. Adipiscing feugiat pharetra imperdiet cursus ultrices. Penatibus quis cursus mollis adipiscing.</p>
    <p class="body">Nunc lectus mi sed enim nisi pretium enim augue. Aliquam quam amet in diam in arcu. Tincidunt vulputate augue quam in eu. Urna tortor iaculis enim turpis fringilla sagittis at et faucibus. Nunc eu purus sit hendrerit. Sit lacus a tristique sed in nibh rutrum faucibus. Accumsan orci iaculis sit morbi sit tortor facilisis. Odio turpis massa sit non facilisi risus. Elementum eu id vitae arcu porta ridiculus. Eget orci enim lacus sed est in egestas maecenas nisi. Eget ultrices lectus tincidunt in laoreet duis nulla. Faucibus consectetur tincidunt aenean sed vitae velit imperdiet. Ut cursus amet pharetra vivamus. Aliquam eleifend aliquam tortor lorem feugiat nisl. Faucibus enim diam at sed senectus nam duis.</p>
    <p class="body">At ultrices risus in ante est praesent. Aliquam gravida condimentum non sed semper. Arcu ornare odio tincidunt in a eu netus nec mattis.</p>
    <div class="sign-off">Thanks,</div>
    <div class="signature" role="img" aria-label="Handwritten signature"></div>
    <div class="sign-name">DR MAYLA CORWEN</div>
    <div>MD FRACP FRCPC PhD BSc</div>
    <div>Consultant Endocrinologist</div>
  </div>
  <div class="foot-rule"></div>
  <div class="contact" style="left:43px;top:621px"><svg viewBox="0 0 10 10"><path d="M5 9Q1 5 1 4a4 4 0 0 1 8 0q0 1-4 5z" fill="none" stroke="currentColor"/><circle cx="5" cy="4" r="1.3" fill="currentColor"/></svg>Suite 4, 282 Falcon Street, Richmond, VIC 3121</div>
  <div class="contact" style="right:43px;top:621px">www.drmaylacorwen.com.au<svg viewBox="0 0 10 10"><circle cx="5" cy="5" r="4" fill="currentColor"/></svg></div>
</article>

<h2 class="section-label" style="left:449px;top:2029px">NOTEPAD DESIGN</h2>

<article class="notepad">
  <div class="tab"></div>
  <div class="brand" style="left:24px;top:19px"><span class="brand-name">Dr Mayla Corwen</span><span class="brand-sub">ENDOCRINOLOGY</span></div>
  <div class="head-rule" style="left:120px;top:37px;width:186px;background:var(--brand-mauve)"></div>
  <div class="date-field">Date: <span></span></div>
  <div class="lines"></div>
  <div class="foot-rule" style="left:24px;width:258px;top:410px"></div>
  <div class="contact" style="left:24px;top:417px;font-size:4px"><svg viewBox="0 0 10 10"><path d="M2 1l2 0 1 2-1 1q1 2 3 3l1-1 2 1 0 2q-6 0-8-8z" fill="currentColor"/></svg>03 9417 2253</div>
  <div class="contact" style="left:118px;top:417px;font-size:4px"><svg viewBox="0 0 10 10"><rect x="1" y="2" width="8" height="6" fill="none" stroke="currentColor"/><path d="M1 2l4 3 4-3" fill="none" stroke="currentColor"/></svg>admin@drmaylacorwen.com.au</div>
  <div class="contact" style="left:235px;top:417px;font-size:4px"><svg viewBox="0 0 10 10"><circle cx="5" cy="5" r="4" fill="currentColor"/></svg>www.drmaylacorwen.com.au</div>
</article>

</body>
</html>
```